Security doors and flyscreens

We need business cards for our company called K & R Traders. We quote, manufacture and install security doors and flyscreens.

Industry/Entity Type

Security

Contact Information for Business Card

K & R TRADERS
17 Larkfield Ave. Brackenvale 3091
Ph: 8127 5506
Fax: 8127 5502
Colin: 0417 952 160
Email: gatemakerhub@mailbox-example.net

```html
<!DOCTYPE html>
<html lang="en">
<head>
<meta charset="utf-8">
<title>K &amp; R Traders – Business Card</title>
<link href="https://fonts.googleapis.com/css2?family=Quicksand:wght@400;500;700&display=swap" rel="stylesheet">
<style>
  :root {
    --stage: #e6e8e9;
    --card-white: #ffffff;
    --ink-dark: #2b3032;
    --ink-grey: #6d7275;
    --brand-orange: #f47b20;
    --brand-teal: #4fd6d6;
    --divider: #b9bdbf;
    --back-centre: #5f696c;
    --back-edge: #3a4245;
    --on-dark: #ffffff;
  }
  * { margin: 0; padding: 0; box-sizing: border-box; }
  html, body { width: 1200px; height: 1200px; overflow: hidden; }
  body {
    background: var(--stage);
    font-family: "Quicksand", sans-serif;
    display: flex;
    flex-direction: column;
    align-items: center;
    justify-content: center;
    gap: 60px;
  }
  .card {
    position: relative;
    width: 900px;
    height: 514px;
    overflow: hidden;
  }
  .card--front { background: var(--card-white); }
  .card--back {
    background: radial-gradient(ellipse at 50% 45%, var(--back-centre) 0%, var(--back-edge) 100%);
    display: flex;
    align-items: center;
    justify-content: center;
  }
  .brand-name {
    font-family: "Quicksand", sans-serif;
    font-weight: 700;
    font-size: 64px;
    line-height: 1.05;
    letter-spacing: 1px;
    text-align: center;
    color: var(--ink-dark);
  }
  .card--front .brand-name {
    position: absolute;
    left: 42px;
    top: 150px;
    width: 370px;
  }
  .card--back .brand-name { color: var(--on-dark); font-size: 76px; }
  .divider {
    position: absolute;
    left: 443px;
    top: 133px;
    width: 2px;
    height: 225px;
    background: var(--divider);
  }
  .contact {
    position: absolute;
    left: 466px;
    top: 124px;
  }
  .contact__address {
    color: var(--brand-orange);
    font-size: 33px;
    font-weight: 500;
    line-height: 1.05;
    margin-bottom: 28px;
  }
  .contact__list { list-style: none; }
  .contact__item {
    font-size: 20px;
    line-height: 1.55;
    color: var(--ink-grey);
    white-space: nowrap;
  }
  .contact__label { color: var(--brand-teal); }
  .card__bands {
    position: absolute;
    left: 0;
    bottom: 0;
    width: 900px;
    height: 60px;
  }
</style>
</head>
<body>
  <section class="card card--front" aria-label="Business card front">
    <div class="brand-name">K &amp; R<br>Traders</div>
    <div class="divider"></div>
    <div class="contact">
      <p class="contact__address">17 Larkfield Ave.<br>Brackenvale 3091</p>
      <ul class="contact__list">
        <li class="contact__item"><span class="contact__label">Colin:</span> 0417 952 160</li>
        <li class="contact__item"><span class="contact__label">Ph:</span> 8127 5506</li>
        <li class="contact__item"><span class="contact__label">Fax:</span> 8127 5502</li>
        <li class="contact__item"><span class="contact__label">Email:</span> gatemakerhub@mailbox-example.net</li>
      </ul>
    </div>
    <svg class="card__bands" viewBox="0 0 900 60" aria-hidden="true">
      <polygon points="0,10 462,10 455,18 0,18" fill="var(--brand-teal)"/>
      <polygon points="0,28 452,28 478,4 900,4 900,60 0,60" fill="var(--brand-orange)"/>
    </svg>
  </section>

  <section class="card card--back" aria-label="Business card back">
    <div class="brand-name">K &amp; R<br>Traders</div>
  </section>
</body>
</html>
```